Vela Stewardship Business Card design

We need a creative business card design for our hospitality management company
We need the following information:
Our business Logo: Vela Stewardship
Name: Mara Dobrinsky
Phone number: 0458 317 642
Email: mara@velastewardship.com.au
Address: 214/53 Penrose Street, Kelland Bay 3208
Web: www.velastewardship.com.au
I need the design to be a working file so that I can insert the names and numbers of the other staff members of our business.
The cards need to be 90 x 40mm
Thanks
Industry/Entity Type
Hospitality
Look and feel

```html
<!DOCTYPE html>
<html lang="en">
<head>
<meta charset="utf-8">
<title>Vela Stewardship Business Card</title>
<link href="https://fonts.googleapis.com/css2?family=Arimo:wght@400;700&display=swap" rel="stylesheet">
<style>
  :root {
    --backdrop: #e9ecef;
    --card-white: #ffffff;
    --navy: #14385e;
    --brand-blue: #1b84d6;
    --pale-blue: #d8ebf9;
    --deep-blue: #0a3d6b;
    --mid-blue: #1665a6;
    --ink: #333a40;
  }
  * { margin: 0; padding: 0; box-sizing: border-box; }
  html, body {
    width: 1200px; height: 893px; overflow: hidden;
    background: var(--backdrop);
    font-family: "Arimo", Arial, sans-serif;
  }
  .sheet { position: relative; width: 1200px; height: 893px; }
  .card {
    position: absolute; left: 240px; width: 720px; height: 320px;
    border-radius: 4px; overflow: hidden;
    box-shadow: 0 6px 18px rgba(0,0,0,0.18);
  }
  .card-back {
    top: 84px;
    background: linear-gradient(160deg, var(--mid-blue) 0%, var(--deep-blue) 70%, #072c4f 100%);
    display: flex; align-items: center; justify-content: center; gap: 18px;
  }
  .back-mark { width: 44px; height: 44px; background: #ffffff; }
  .back-name {
    color: #ffffff; font-weight: 700; font-size: 42px;
    text-transform: uppercase; letter-spacing: 0.5px;
  }
  .card-front { top: 489px; background: var(--card-white); }
  .front-brand {
    position: absolute; left: 52px; top: 118px;
    display: flex; align-items: center; gap: 12px;
  }
  .front-mark { width: 28px; height: 28px; background: var(--navy); }
  .front-name {
    color: var(--navy); font-weight: 700; font-size: 26px;
    text-transform: uppercase; letter-spacing: 0.3px;
  }
  .contact {
    position: absolute; right: 34px; top: 28px;
    text-align: right; color: var(--ink);
    font-size: 15px; line-height: 21px;
  }
  .contact-person {
    color: var(--navy); font-weight: 700; font-size: 19px;
    margin-bottom: 16px;
  }
  .base-tint {
    position: absolute; left: 0; bottom: 0; width: 720px; height: 44px;
    background: linear-gradient(to bottom, rgba(255,255,255,0), var(--pale-blue));
  }
  .base-band {
    position: absolute; left: 0; bottom: 34px; width: 720px; height: 10px;
    background: var(--brand-blue);
  }
  .base-rule {
    position: absolute; left: 0; bottom: 56px; width: 720px; height: 2px;
    background: var(--pale-blue);
  }
</style>
</head>
<body>
<main class="sheet">
  <section class="card card-back" aria-label="Card back">
    <span class="back-mark"></span>
    <span class="back-name">Vela Stewardship</span>
  </section>

  <section class="card card-front" aria-label="Card front">
    <div class="base-rule"></div>
    <div class="base-band"></div>
    <div class="base-tint"></div>

    <div class="front-brand">
      <span class="front-mark"></span>
      <span class="front-name">Vela Stewardship</span>
    </div>

    <div class="contact">
      <p class="contact-person">Mara Dobrinsky</p>
      <p>0458 317 642</p>
      <p>mara@velastewardship.com.au</p>
      <p>214/53 Penrose Street</p>
      <p>Kelland Bay 3208</p>
      <p>www.velastewardship.com.au</p>
    </div>
  </section>
</main>
</body>
</html>
```